Design of Postcards for pairvo.ch - to promote this online dating platform

Tobias and me, we operate a dating platform called
pairvo.ch.

pairvo.ch

On this platform you find members with whom you can spend your spare time, share your hobbies or find a partner or a friend.

we need 5 different postcard designs; means, we will send the postcards to our members; they will send the postcards to their friends and colleagues in order to find and win new members for our platform.

we are looking forward receiving your draft designs. for postcards in the format DIN A6 (mm 105 × 148). these postcards should promote and communicate our brand, our colors, our url, pairvo.ch, and the topic of finding a friend, a colleague, a partner, someone to spend your time or life with.

thnx, Tobias 6 Luca

Target Market(s)

adults age 30-45

Industry/Entity Type

Dating

Font styles to use
Decorative
Script

Requirements
Must have
• please find logo of pairvo.ch on our website, pairvo.ch
• if possible using colors of pairvo.ch, please see website
• postcards should appeal men and women.

```html
<!DOCTYPE html>
<html lang="en">
<head>
<meta charset="utf-8">
<title>pairvo.ch – Postcard</title>
<link rel="stylesheet" href="https://fonts.googleapis.com/css2?family=Montserrat:wght@600;700&family=Open+Sans:wght@400&family=Sacramento&display=swap">
<style>
  :root {
    --page-bg: #2b2b2d;
    --brand-crimson: #9a0f3b;
    --brand-crimson-deep: #8a0c35;
    --ink-light: #ffffff;
    --photo-white: #fbf9f8;
    --photo-skin: #ecc9b8;
    --photo-skin-deep: #d9a791;
    --photo-hair: #9a7c6c;
    --photo-sweater: #bfc0c3;
  }
  html, body {
    margin: 0;
    padding: 0;
    width: 1200px;
    height: 960px;
    overflow: hidden;
    background: var(--page-bg);
  }
  .postcard {
    position: absolute;
    left: 96px;
    top: 124px;
    width: 1008px;
    height: 713px;
    background: linear-gradient(120deg, var(--brand-crimson) 0%, var(--brand-crimson-deep) 100%);
    overflow: hidden;
    color: var(--ink-light);
  }
  .postcard-art {
    position: absolute;
    inset: 0;
    width: 100%;
    height: 100%;
  }
  .brand {
    position: absolute;
    right: 66px;
    top: 44px;
  }
  .brand-name {
    display: flex;
    align-items: center;
    gap: 10px;
    font-family: "Montserrat", sans-serif;
    font-weight: 700;
    font-size: 41px;
    line-height: 1;
    text-transform: uppercase;
  }
  .brand-dot {
    width: 40px;
    height: 40px;
    border-radius: 50%;
    background: var(--ink-light);
  }
  .brand-tagline {
    margin-top: 8px;
    margin-left: 50px;
    font-family: "Montserrat", sans-serif;
    font-weight: 600;
    font-size: 11.5px;
    letter-spacing: 1.3px;
    text-transform: uppercase;
  }
  .message {
    position: absolute;
    right: 66px;
    top: 170px;
    margin: 0;
    text-align: right;
    font-family: "Sacramento", cursive;
    font-size: 40px;
    line-height: 71px;
    font-weight: 400;
  }
  .web-address {
    position: absolute;
    right: 66px;
    top: 640px;
    font-family: "Open Sans", sans-serif;
    font-size: 26px;
    line-height: 1;
  }
</style>
</head>
<body>
  <main class="postcard">
    <svg class="postcard-art" viewBox="0 0 840 594" preserveAspectRatio="none">
      <defs>
        <radialGradient id="ghostTone" cx="0.5" cy="0.5" r="0.5">
          <stop offset="0" stop-color="#ffffff" stop-opacity="0.12"/>
          <stop offset="1" stop-color="#ffffff" stop-opacity="0"/>
        </radialGradient>
        <linearGradient id="photoBase" x1="0" y1="0" x2="0" y2="1">
          <stop offset="0" stop-color="var(--photo-white)"/>
          <stop offset="0.45" stop-color="#f3e6df"/>
          <stop offset="1" stop-color="#e4e0df"/>
        </linearGradient>
        <radialGradient id="photoWarmLeft" cx="0.38" cy="0.42" r="0.32">
          <stop offset="0" stop-color="var(--photo-skin-deep)" stop-opacity="0.85"/>
          <stop offset="0.6" stop-color="var(--photo-skin)" stop-opacity="0.55"/>
          <stop offset="1" stop-color="var(--photo-skin)" stop-opacity="0"/>
        </radialGradient>
        <radialGradient id="photoWarmRight" cx="0.62" cy="0.5" r="0.3">
          <stop offset="0" stop-color="var(--photo-skin-deep)" stop-opacity="0.7"/>
          <stop offset="0.55" stop-color="var(--photo-hair)" stop-opacity="0.35"/>
          <stop offset="1" stop-color="var(--photo-hair)" stop-opacity="0"/>
        </radialGradient>
        <linearGradient id="photoLower" x1="0" y1="0" x2="0" y2="1">
          <stop offset="0.55" stop-color="var(--photo-sweater)" stop-opacity="0"/>
          <stop offset="1" stop-color="var(--photo-sweater)" stop-opacity="0.75"/>
        </linearGradient>
        <clipPath id="bubbleClip">
          <path d="M 500 412 A 255 255 0 1 0 365 529 L 520 562 Z"/>
        </clipPath>
      </defs>

      <g class="background-photo" role="img" aria-label="Faded enlargement of the couple photo across the card">
        <ellipse cx="40" cy="170" rx="150" ry="190" fill="url(#ghostTone)"/>
        <ellipse cx="560" cy="290" rx="190" ry="240" fill="url(#ghostTone)"/>
        <ellipse cx="700" cy="430" rx="160" ry="170" fill="url(#ghostTone)"/>
      </g>

      <g class="speech-bubble" role="img" aria-label="Photo of a laughing couple cheek to cheek, forming a heart with their hands" clip-path="url(#bubbleClip)">
        <rect x="0" y="0" width="840" height="594" fill="url(#photoBase)"/>
        <rect x="0" y="0" width="560" height="594" fill="url(#photoWarmLeft)"/>
        <rect x="0" y="0" width="560" height="594" fill="url(#photoWarmRight)"/>
        <rect x="0" y="0" width="560" height="594" fill="url(#photoLower)"/>
      </g>
    </svg>

    <header class="brand">
      <div class="brand-name"><span class="brand-dot"></span>pairvo.ch</div>
      <div class="brand-tagline">Die Partnersuche der Schweiz</div>
    </header>

    <p class="message">
      find members<br>
      with whom you can<br>
      spend your spare time,<br>
      share your hobbies<br>
      or find a partner<br>
      or a friend.
    </p>

    <div class="web-address">www.pairvo.ch</div>
  </main>
</body>
</html>
```